Dog care service needs advertising poster

Our company is Pawfield Haven. We provide care for dogs while their owners are away, either through home visits or a holiday stay in the homes of carefully selected minders. Our existing website & Facebook cover should provide all the colour cues for a poster - namely blues, blondes and grey. We have an existing logo (provided). We can feature the same imagery from our website as I have purchased the rights to the stock images.

www.pawfieldhaven.com.au
www.facebook.com/pawfieldhavenau

This brief is for design of a poster that can be placed in vet surgeries, groomers, on community noticeboards. It should be scalable to print in three sizes, A5, A4 & A3.

We wish to clearly communicate our three areas of service "dog minding, home visits, dog walking".

We would like to have the files ready for upload to Printlorra (or similar) for immediate printing.

Target Market(s)

Dog owners who love their dogs like family.

Industry/Entity Type

Advertising

Font styles to use
Sans Serif

Colors
33a6d7
3276b5

Requirements
Must have
• Logo
• www.pawfieldhaven.com.au
• Telephone number
• Three services - Dog Minding, Home Visits, Dog Walking
Nice to have
• use of our existing stock photography to highlight the three areas of service - Dog minding, home visits, dog walking. Existing colour palette - blues, blondes and grey.
• Text that can be used:
• Western Sydney’s complete dog care service.
• Dog Minding - Your dog stays in the home of one of our carefully selected minders.Treated like part of the family, they enjoy all the creature comforts they are used to.
• Home Visits - We visit your dog at your home for feeding, walking and playtime. Short of long visits available.
• Dog Walking - If you can't walk your dog for any reason we are here to help. 1/2 hour or hourly walks available.
• Contact us today for a tailored package to meet your needs.
Should not have
• Any additional illustrations beyond the logo.

```html
<!DOCTYPE html>
<html lang="en">
<head>
<meta charset="utf-8">
<title>Pawfield Haven – Dog Care Poster</title>
<link rel="stylesheet" href="https://fonts.googleapis.com/css2?family=Open+Sans:wght@400;600;700&display=swap">
<style>
  :root {
    --sky-blue: #33a6d7;
    --deep-blue: #3276b5;
    --shadow-blue: #2f9bd6;
    --slate: #3a4556;
    --white: #ffffff;
    --backdrop: #d9d6d2;
    --photo-sky: #bcd9ee;
    --photo-grass: #7fb041;
    --photo-coat: #6b5a4c;
  }
  html, body {
    margin: 0;
    padding: 0;
    width: 1200px;
    height: 935px;
    overflow: hidden;
    background: var(--backdrop);
    font-family: "Open Sans", Arial, sans-serif;
  }
  .canvas {
    position: relative;
    width: 1200px;
    height: 935px;
  }
  .poster {
    position: absolute;
    left: 38px;
    top: 35px;
    width: 1125px;
    height: 865px;
    background: var(--white);
    box-shadow: 0 4px 14px rgba(0,0,0,0.25);
    overflow: hidden;
  }
  .poster-art {
    position: absolute;
    left: -38px;
    top: -35px;
    width: 1200px;
    height: 935px;
  }
  .brand {
    position: absolute;
    left: 34px;
    top: 58px;
    display: flex;
    align-items: center;
    gap: 18px;
  }
  .brand-mark {
    width: 92px;
    height: 92px;
    border-radius: 50%;
    background: var(--sky-blue);
  }
  .brand-name {
    margin: 0;
    font-weight: 600;
    font-size: 44px;
    line-height: 42px;
    color: var(--slate);
    letter-spacing: -0.5px;
  }
  .tagline {
    position: absolute;
    right: 73px;
    top: 382px;
    margin: 0;
    text-align: right;
    font-weight: 400;
    font-size: 33px;
    line-height: 54px;
    color: var(--white);
    text-shadow: 1px 1px 2px rgba(0,0,0,0.45);
  }
  .services {
    position: absolute;
    left: 120px;
    top: 690px;
    margin: 0;
    padding: 0;
    list-style: none;
    display: flex;
    gap: 34px;
    font-size: 30px;
    color: var(--sky-blue);
  }
  .services li {
    display: flex;
    align-items: center;
    gap: 10px;
  }
  .services li::before {
    content: "";
    width: 16px;
    height: 16px;
    border-radius: 50%;
    background: var(--deep-blue);
  }
  .contact {
    position: absolute;
    left: 0;
    right: 0;
    top: 790px;
    display: flex;
    justify-content: center;
    align-items: center;
    gap: 30px;
    color: var(--white);
    font-weight: 700;
  }
  .contact-item {
    display: flex;
    align-items: center;
    gap: 14px;
  }
  .contact-phone { font-size: 33px; }
  .contact-web { font-size: 30px; }
</style>
</head>
<body>
<div class="canvas">
  <div class="poster">
    <svg class="poster-art" viewBox="0 0 1200 935" xmlns="http://www.w3.org/2000/svg">
      <defs>
        <linearGradient id="photo-tones" x1="0" y1="0" x2="0" y2="1">
          <stop offset="0" stop-color="var(--photo-sky)"/>
          <stop offset="0.45" stop-color="#a9c9c9"/>
          <stop offset="0.62" stop-color="var(--photo-grass)"/>
          <stop offset="1" stop-color="#5f9a2e"/>
        </linearGradient>
        <radialGradient id="photo-subject" cx="0.5" cy="0.55" r="0.35">
          <stop offset="0" stop-color="var(--photo-coat)" stop-opacity="0.55"/>
          <stop offset="1" stop-color="var(--photo-coat)" stop-opacity="0"/>
        </radialGradient>
        <path id="cloud" d="M230,620 C150,625 110,560 115,480 C120,395 190,345 270,350 C300,348 320,352 335,358 C350,180 470,90 640,90 C800,90 900,190 905,300 C990,285 1060,330 1080,380 C1140,400 1140,560 1070,600 C1030,640 960,650 900,625 C860,690 750,700 690,660 C640,690 540,690 490,650 C420,680 340,670 300,630 C280,625 255,620 230,620 Z"/>
      </defs>
      <use href="#cloud" class="cloud-shadow" fill="var(--shadow-blue)" transform="translate(20,14)"/>
      <g role="img" aria-label="Photo of a happy tricolour shepherd dog sitting in green grass under a pale blue sky">
        <use href="#cloud" fill="url(#photo-tones)"/>
        <use href="#cloud" fill="url(#photo-subject)"/>
      </g>
      <path class="band-edge" d="M38,818 Q600,768 1163,818 L1163,835 L38,835 Z" fill="var(--deep-blue)"/>
      <path class="contact-band" d="M38,828 Q600,780 1163,828 L1163,900 L38,900 Z" fill="var(--sky-blue)"/>
    </svg>

    <div class="brand">
      <span class="brand-mark" aria-hidden="true"></span>
      <h1 class="brand-name">Pawfield<br>Haven</h1>
    </div>

    <p class="tagline">Western Sydney’s<br>Complete Dog care<br>Service</p>

    <ul class="services">
      <li>Dog Minding</li>
      <li>Home Visits</li>
      <li>Dog Walking</li>
    </ul>

    <div class="contact">
      <span class="contact-item contact-phone">
        <svg width="42" height="42" viewBox="0 0 42 42" aria-hidden="true">
          <circle cx="21" cy="21" r="19" fill="none" stroke="#fff" stroke-width="3"/>
          <path d="M15,11 l4,0 l2,6 l-3,2 q2,5 6,7 l2,-3 l6,2 l0,4 q-2,3 -6,2 q-12,-4 -14,-15 q0,-4 3,-5 Z" fill="#fff"/>
        </svg>
        0412 555 318
      </span>
      <span class="contact-item contact-web">
        <svg width="42" height="42" viewBox="0 0 42 42" aria-hidden="true">
          <g fill="none" stroke="#fff" stroke-width="2.5">
            <circle cx="21" cy="21" r="18"/>
            <ellipse cx="21" cy="21" rx="8" ry="18"/>
            <line x1="3" y1="21" x2="39" y2="21"/>
            <path d="M6,12 H36 M6,30 H36"/>
          </g>
        </svg>
        www.pawfieldhaven.com.au
      </span>
    </div>
  </div>
</div>
</body>
</html>
```